TALRENO Business Cards

We require a business card for our company that provides IT consulting services. We already have a logo that needs to be used on the card. We want a clean professional looking design that incorporates our colours. Our main focus is providing managed services to business, which involves us looking after all of their IT requirements including managing servers/networks, projects, and procurement.

Industry/Entity Type

Information Technology

Requirements
Must have
• our logo, contact information, name, title, phone numbers

```html
<!DOCTYPE html>
<html lang="en">
<head>
<meta charset="utf-8">
<title>TALRENO Business Cards</title>
<link href="https://fonts.googleapis.com/css2?family=Ubuntu:ital,wght@0,400;0,500;1,700&display=swap" rel="stylesheet">
<style>
  :root {
    --brand-blue: #2a8fcc;
    --band-top: #2b97d2;
    --band-bottom: #1d6c9e;
    --card-white: #ffffff;
    --backdrop: #e9ecef;
  }
  html, body {
    margin: 0;
    padding: 0;
    width: 1200px;
    height: 1200px;
    overflow: hidden;
    background: var(--backdrop);
    font-family: "Ubuntu", sans-serif;
  }
  .canvas {
    position: relative;
    width: 1200px;
    height: 1200px;
  }
  .card {
    position: absolute;
    background: var(--card-white);
    overflow: hidden;
  }
  .card-front {
    left: 218px;
    top: 131px;
    width: 752px;
    height: 429px;
  }
  .card-front .accent-bar {
    position: absolute;
    left: 0;
    right: 0;
    bottom: 0;
    height: 12px;
    background: var(--brand-blue);
  }
  .wordmark {
    font-family: "Ubuntu", sans-serif;
    font-weight: 500;
    color: var(--brand-blue);
    letter-spacing: 0.04em;
    margin: 0;
    line-height: 1;
  }
  .card-front .wordmark {
    position: absolute;
    left: 0;
    right: 0;
    top: 178px;
    text-align: center;
    font-size: 90px;
  }
  .card-back {
    left: 217px;
    top: 630px;
    width: 766px;
    height: 438px;
  }
  .card-back .wordmark {
    position: absolute;
    left: 602px;
    top: 43px;
    font-size: 24px;
  }
  .holder-name {
    position: absolute;
    left: 48px;
    top: 78px;
    margin: 0;
    font-size: 54px;
    font-weight: 500;
    color: var(--brand-blue);
    line-height: 1;
  }
  .holder-title {
    position: absolute;
    left: 55px;
    top: 125px;
    margin: 0;
    font-size: 24px;
    font-weight: 400;
    color: var(--brand-blue);
    line-height: 1;
  }
  .contact-band {
    position: absolute;
    left: 0;
    right: 0;
    top: 219px;
    bottom: 0;
    background: linear-gradient(to bottom, var(--band-top), var(--band-bottom));
    color: var(--card-white);
  }
  .contact-list {
    position: absolute;
    left: 54px;
    top: 50px;
    margin: 0;
    line-height: 1;
  }
  .contact-label {
    font-size: 26px;
    font-weight: 700;
    font-style: italic;
    margin: 0;
  }
  .contact-value {
    font-size: 21px;
    font-weight: 400;
    margin: 0 0 14px 0;
  }
</style>
</head>
<body>
<main class="canvas">
  <section class="card card-front" aria-label="Business card front">
    <p class="wordmark">TALRENO</p>
    <div class="accent-bar"></div>
  </section>

  <section class="card card-back" aria-label="Business card back">
    <p class="wordmark">TALRENO</p>
    <h1 class="holder-name">YOUR NAME</h1>
    <p class="holder-title">job title</p>
    <div class="contact-band">
      <dl class="contact-list">
        <dt class="contact-label">email.</dt>
        <dd class="contact-value" style="margin-left:0">youremail@yourdomain.com</dd>
        <dt class="contact-label">phone.</dt>
        <dd class="contact-value" style="margin-left:0">123.456.7891</dd>
      </dl>
    </div>
  </section>
</main>
</body>
</html>
```